Business cards design on a high standard

We advise clients on insurance and financial matters, since these clients pay for our advice, the design should have a high standard. Our logo should be included. From the colors we are open for everything.

Colors

Designer to choose colors to be used in the design.

```html
<!DOCTYPE html>
<html lang="en">
<head>
<meta charset="utf-8">
<title>Alpine Counsel – Business Card</title>
<link rel="stylesheet" href="https://fonts.googleapis.com/css2?family=Arimo:wght@400;700&display=swap">
<style>
  :root {
    --backdrop: #e6e7e9;
    --card: #f6f7f7;
    --brand-red: #e91e25;
    --accent-grey: #a4a5a7;
    --ink: #1d1d1f;
    --white: #ffffff;
  }
  * { margin: 0; padding: 0; box-sizing: border-box; }
  html, body {
    width: 1200px;
    height: 545px;
    overflow: hidden;
    background: var(--backdrop);
    font-family: "Arimo", Arial, sans-serif;
  }
  .canvas { position: relative; width: 1200px; height: 545px; }

  .card {
    position: absolute;
    top: 156px;
    width: 516px;
    height: 310px;
    background: var(--card);
    overflow: hidden;
  }
  .card--front { left: 60px; }
  .card--back { left: 624px; width: 517px; }

  .card__shapes { position: absolute; inset: 0; }

  .wordmark {
    position: absolute;
    color: var(--brand-red);
    font-weight: 700;
    font-size: 24px;
    letter-spacing: 1px;
    line-height: 1.1;
    text-align: center;
    white-space: nowrap;
  }
  .wordmark span { display: block; }
  .card--front .wordmark { left: 37px; width: 181px; top: 127px; }
  .card--back .wordmark { left: 0; right: 0; top: 112px; }

  .holder-name {
    position: absolute;
    left: 311px;
    top: 82px;
    color: var(--white);
    font-weight: 700;
    font-size: 20px;
    letter-spacing: 0.5px;
  }
  .holder-name__rule {
    position: absolute;
    left: 316px;
    top: 111px;
    width: 54px;
    height: 2px;
    background: var(--white);
  }
  .contact-list {
    position: absolute;
    left: 311px;
    top: 157px;
    list-style: none;
    color: var(--white);
    font-size: 15px;
  }
  .contact-list li { height: 26px; line-height: 18px; }

  .address {
    position: absolute;
    left: 0; right: 0;
    top: 184px;
    text-align: center;
    color: var(--ink);
    font-size: 14.5px;
  }
  .card__footer-band {
    position: absolute;
    left: 0; right: 0;
    top: 262px;
    bottom: 0;
    background: var(--brand-red);
  }
</style>
</head>
<body>
<main class="canvas">

  <section class="card card--front" aria-label="Card front">
    <svg class="card__shapes" width="516" height="310" viewBox="0 0 516 310" aria-hidden="true">
      <polygon fill="var(--brand-red)" points="246,0 516,0 516,310 271,310 271,152 246,129"/>
      <polygon fill="var(--accent-grey)" points="240,140 247,140 266,160 266,310 254,310 254,164 240,150"/>
    </svg>
    <div class="wordmark"><span>ALPINE</span><span>COUNSEL</span></div>
    <h1 class="holder-name">YOUR NAME</h1>
    <div class="holder-name__rule"></div>
    <ul class="contact-list">
      <li>(000) 000-0000</li>
      <li>(000) 000-0000</li>
      <li>your@email.com</li>
      <li>www.yourwebsite.com</li>
    </ul>
  </section>

  <section class="card card--back" aria-label="Card back">
    <div class="wordmark"><span>ALPINE</span><span>COUNSEL</span></div>
    <p class="address">Your Address, City, State, ZIP&nbsp; 00000, Country</p>
    <div class="card__footer-band"></div>
  </section>

</main>
</body>
</html>
```